Elegant Business Card for Technology Company

Client is a supplier of innovative industrial communications and automation equipment since 2002. This contest is to gather fresh ideas for a redesign of the existing business card. Client is looking for design that best communicates tagline "Industrial Networking and Computing Specialist".

Design submissions should look modern, clean, elegant and professional. It should not be cluttered. Use white as the primary colour. Orange and black as secondary colour. Refer to jpeg File 1 on the current design.

Fonts used by Client used include Arial Regular, Arial Black, Roboto Regular, Roboto Black and Lato.

The winning design will be sent for offset printing using super white 250gsm artcard paper (open for suggestions).

Target Market(s)

System Engineers, Project Managers, Purchasing Managers from companies providing engineering services for Smart Cities.

Industry/Entity Type

Information Technology

Contact Information for Business Card

Refer to PDF File 3 for Business Card Details. Priority of short contact information would be as follows Name > Job Title > Email > Mobile > Web > Tel > Fax > Business Address >UEN (UEN represents company registration number)

Font styles to use
Sans Serif

Colors
ffffff
f37122
000000
5c5c5c

Requirements
Must have
• Refer to AI File 2 (Company Logo) & PDF File 3 (Information on Namecard)
Should not have
• No QR codes
• No Social Media Icons
• Do not create full Black or Orange colour background

```html
<!DOCTYPE html>
<html lang="en">
<head>
<meta charset="utf-8">
<title>KVR Business Card</title>
<link rel="stylesheet" href="https://fonts.googleapis.com/css2?family=Archivo+Black&family=Roboto:wght@400;700;900&family=Roboto+Condensed:ital,wght@0,400;0,700;1,400&display=swap">
<style>
  :root {
    --orange: #f37122;
    --orange-soft: #f68a45;
    --white: #ffffff;
    --black: #000000;
    --ink: #1e1e1e;
    --grey: #5c5c5c;
    --backdrop: #e6e6e6;
  }
  * { margin: 0; padding: 0; box-sizing: border-box; }
  html, body { width: 1200px; height: 900px; overflow: hidden; }
  body { background: var(--backdrop); position: relative; }

  .card {
    position: absolute;
    left: 300px;
    width: 600px;
    height: 360px;
    overflow: hidden;
    box-shadow: 0 6px 18px rgba(0,0,0,0.18);
  }
  .card-back { top: 60px; background: var(--orange); }
  .card-front { top: 470px; background: var(--white); }

  .card-shape { position: absolute; inset: 0; width: 600px; height: 360px; }

  /* back side */
  .service-list {
    position: absolute;
    left: 0; top: 36px;
    width: 600px;
    list-style: none;
  }
  .service {
    height: 27px;
    line-height: 27px;
    padding-left: 162px;
    font-family: "Archivo Black", "Arial Black", sans-serif;
    font-size: 13.5px;
    letter-spacing: 0.3px;
    text-transform: uppercase;
    white-space: nowrap;
  }
  .service-band { background: var(--white); color: var(--orange); margin-left: 150px; padding-left: 12px; }
  .service-plain { color: var(--white); }

  /* front side */
  .brand {
    position: absolute;
    left: 52px; top: 90px;
    display: flex; align-items: center; gap: 14px;
  }
  .brand-dot { width: 62px; height: 62px; border-radius: 50%; background: var(--orange); }
  .brand-name {
    font-family: "Roboto", Arial, sans-serif;
    font-weight: 900;
    font-size: 64px;
    line-height: 1;
    color: var(--black);
    letter-spacing: 2px;
  }
  .address {
    position: absolute;
    left: 48px; top: 232px;
    font-family: "Roboto Condensed", Arial, sans-serif;
    font-style: italic;
    font-size: 19px;
    line-height: 26px;
    color: var(--orange);
  }
  .contact-block {
    position: absolute;
    left: 368px; top: 44px;
    width: 210px;
    font-family: "Roboto Condensed", Arial, sans-serif;
  }
  .person-name { font-weight: 700; font-size: 27px; color: var(--ink); line-height: 1.1; }
  .person-title {
    font-weight: 700; font-size: 17px; color: var(--white);
    padding-bottom: 4px; border-bottom: 1.5px solid var(--white);
    margin-bottom: 12px;
  }
  .contact-line { font-size: 16px; line-height: 23px; color: var(--ink); white-space: nowrap; }
  .contact-line strong { font-weight: 700; }
  .uen { margin-top: 22px; font-size: 15px; color: var(--ink); }
  .uen span { font-size: 19px; }
</style>
</head>
<body>

<section class="card card-back" aria-label="Card back">
  <svg class="card-shape" viewBox="0 0 600 360">
    <circle cx="-10" cy="150" r="145" fill="var(--white)"/>
    <circle cx="-10" cy="150" r="137" fill="var(--orange-soft)" role="img" aria-label="Dotted circle pattern area"/>
  </svg>
  <ul class="service-list">
    <li class="service service-band">Industrial Networking</li>
    <li class="service service-plain">And Computing Specialist</li>
    <li class="service service-band">Industrial Ethernet / Wireless / Cellular</li>
    <li class="service service-plain">Industrial and Embedded Computing</li>
    <li class="service service-band">Serial / Fieldbus Connectivity</li>
    <li class="service service-plain">IP Video Surveillance</li>
    <li class="service service-band">Remote Automation</li>
  </ul>
</section>

<section class="card card-front" aria-label="Card front">
  <svg class="card-shape" viewBox="0 0 600 360" aria-hidden="true">
    <path d="M300 0 C340 120 318 260 245 360 L600 360 L600 0 Z" fill="var(--orange)"/>
    <path d="M282 0 C320 120 298 258 226 360" fill="none" stroke="var(--orange)" stroke-width="4"/>
  </svg>

  <div class="brand">
    <div class="brand-dot"></div>
    <div class="brand-name">KVR</div>
  </div>

  <address class="address">
    25 Harbour Crescent Delta<br>
    Techpark #04-12 (Lobby B)<br>
    Singapore 400123
  </address>

  <div class="contact-block">
    <div class="person-name">Daniel Hart</div>
    <div class="person-title">Sales Manager</div>
    <div class="contact-line">E-mail: sales@kvrtech.com.sg</div>
    <div class="contact-line">Mobile: +65 8123 4567</div>
    <div class="contact-line">Web: <strong>www.kvrtech.com.sg</strong></div>
    <div class="contact-line">Tel: +65 6123 4500</div>
    <div class="contact-line">Fax: +65 6123 4599</div>
    <div class="contact-line uen">UEN No: <span>200512345K</span></div>
  </div>
</section>

</body>
</html>
```